The Maplewood Learning House Web Page

We need a web design for our Day Care Center based in Brandon, Florida. We are targeting child care and educational services to middle class parents, specially the mother. We would like to see designs that matches attached logo mark. The final design should communicate higher standards for day care and educational services.

Middle class parents in the State of Florida

```html
<!DOCTYPE html>
<html lang="en">
<head>
<meta charset="utf-8">
<title>The Maplewood Learning House</title>
<link href="https://fonts.googleapis.com/css2?family=Raleway:wght@400;500;600&family=Arimo:wght@400;700&display=swap" rel="stylesheet">
<style>
:root{
  --sun:#fdbd35;
  --sun-deep:#f5a91d;
  --navy:#0c2646;
  --navy-card:#14304f;
  --ink:#1e1e1e;
  --muted:#8a8a8a;
  --mist:#e8e8e8;
  --white:#ffffff;
}
*{margin:0;padding:0;box-sizing:border-box}
html,body{width:718px;height:1200px;overflow:hidden;background:var(--white)}
body{position:relative;font-family:"Arimo",Arial,sans-serif;color:var(--ink)}
.abs{position:absolute}

.topbar{left:0;top:0;width:718px;height:68px;background:var(--sun)}
.brand-mark{left:61px;top:8px;width:78px;height:78px;border-radius:50%;background:var(--navy);border:3px solid var(--white);z-index:3}
.brand-name{left:146px;top:24px;font-family:"Raleway",sans-serif;font-weight:600;font-size:13px;color:var(--navy);z-index:3}
.social{top:28px;width:22px;height:22px;border-radius:50%;background:var(--white)}
.social.dark{background:var(--navy)}
.search{left:500px;top:22px;width:158px;height:26px;background:#fcc95a;font-size:9px;color:#5a4a2a;padding:9px 0 0 9px}
.search svg{position:absolute;right:7px;top:5px}

.navbar{left:0;top:68px;width:718px;height:31px;background:var(--navy)}
.nav-item{top:11px;font-size:8.8px;color:var(--white);transform:translateX(-50%);white-space:nowrap}
.nav-item.active{color:var(--sun)}

.hero{left:0;top:99px;width:718px;height:336px;
  background:
    radial-gradient(ellipse 22% 30% at 40% 28%, rgba(246,206,170,.95), rgba(246,206,170,0)),
    radial-gradient(ellipse 20% 28% at 70% 42%, rgba(232,186,150,.95), rgba(232,186,150,0)),
    radial-gradient(ellipse 26% 22% at 38% 8%, rgba(236,214,150,.9), rgba(236,214,150,0)),
    radial-gradient(ellipse 24% 26% at 72% 80%, rgba(226,96,130,.85), rgba(226,96,130,0)),
    radial-gradient(ellipse 22% 24% at 40% 78%, rgba(228,226,214,.95), rgba(228,226,214,0)),
    radial-gradient(ellipse 20% 30% at 92% 12%, rgba(252,246,222,1), rgba(252,246,222,0)),
    linear-gradient(100deg,#e7dccb 0%,#d9c8b0 30%,#cdb497 55%,#e2d2bd 80%,#efe7da 100%)}
.hero-caption{left:4px;top:384px;width:714px;height:51px;background:rgba(255,255,255,.55)}
.hero-caption p{font-family:"Raleway",sans-serif;font-size:14px;color:#1c1c1c;text-align:center;padding-top:20px;letter-spacing:.2px;margin-left:-16px}

.services{left:0;top:435px;width:718px;height:247px;background:var(--navy)}
.section-title{font-family:"Raleway",sans-serif;font-weight:500;font-size:21px;text-align:center;width:718px;left:0}
.services .section-title{top:13px;color:var(--white)}
.service{width:244px;height:55px;background:var(--navy-card)}
.service h3{position:absolute;left:20px;top:8px;font-family:"Raleway",sans-serif;font-weight:500;font-size:11.5px;color:var(--sun)}
.service p{position:absolute;left:21px;top:26px;width:220px;font-size:7.8px;line-height:11px;color:#dfe4ea}
.service-icon{width:34px;height:34px;border-radius:50%;background:var(--sun);border:2px solid #0a1f3a;box-shadow:0 0 0 1px var(--sun)}
.service-icon svg{position:absolute;left:7px;top:7px}

.programs{left:0;top:682px;width:718px;height:259px;background:var(--mist)}
.program{width:130px;height:165px;background:var(--white)}
.program-photo{left:0;top:0;width:130px;height:81px}
.program p{position:absolute;left:2px;top:90px;width:126px;text-align:center;font-size:8.8px;line-height:12px;color:var(--ink)}
.btn{width:69px;height:22px;background:var(--sun);border:1px solid var(--sun-deep);color:var(--white);font-size:8.8px;text-align:center;line-height:20px}

.staff{left:0;top:941px;width:718px;height:235px;background:var(--white)}
.staff .section-title{top:22px;color:var(--navy)}
.staff-intro{left:130px;top:56px;width:458px;text-align:center;font-size:9.4px;line-height:12px;color:var(--muted)}
.member{width:160px;text-align:center}
.avatar{width:68px;height:68px;border-radius:50%;border:2px solid var(--sun);margin:0 auto}
.member h4{font-family:"Raleway",sans-serif;font-weight:500;font-size:9.2px;color:var(--ink);margin-top:12px}
.member p{font-size:9.2px;color:var(--muted);margin-top:6px;white-space:nowrap}

.footer{left:0;top:1176px;width:718px;height:24px;background:var(--navy);color:var(--white);font-size:8.2px;text-align:center;line-height:24px}
</style>
</head>
<body>

<header>
  <div class="abs topbar"></div>
  <div class="abs brand-mark"></div>
  <div class="abs brand-name">The Maplewood Learning House</div>
  <span class="abs social" style="left:392px"></span>
  <span class="abs social dark" style="left:417px"></span>
  <span class="abs social" style="left:442px"></span>
  <span class="abs social" style="left:467px"></span>
  <div class="abs search">search our site
    <svg width="16" height="16" viewBox="0 0 16 16"><circle cx="6.5" cy="6.5" r="5" fill="none" stroke="#0c2646" stroke-width="2"/><line x1="10.2" y1="10.2" x2="14.5" y2="14.5" stroke="#0c2646" stroke-width="2.4" stroke-linecap="round"/></svg>
  </div>
  <nav class="abs navbar">
    <span class="abs nav-item active" style="left:230px">Preferred Vendors</span>
    <span class="abs nav-item" style="left:309px">Real Estate</span>
    <span class="abs nav-item" style="left:386px">Business Co-Ops</span>
    <span class="abs nav-item" style="left:480px">Career Opportunities</span>
    <span class="abs nav-item" style="left:568px">Privacy Policy</span>
    <span class="abs nav-item" style="left:635px">Franchise</span>
  </nav>
</header>

<section>
  <div class="abs hero" role="img" aria-label="Photo of two smiling toddlers playing with colourful toys in a bright room"></div>
  <div class="abs hero-caption"><p>THE MAPLEWOOD LEARNING HOUSE FOR BABYCARE &amp; EDUCATION SERVICES</p></div>
</section>

<section class="abs services">
  <h2 class="abs section-title">Education Services</h2>

  <div class="abs service" style="left:96px;top:60px">
    <h3>HOME SCHOOLSUPPORT</h3>
    <p>Vut sagittis a, magna ridiculus! Scelerisque parturient! Cum duis nunc in, dignissim, porta porta enim, proin turpis .</p>
  </div>
  <div class="abs service-icon" style="left:76px;top:69px"><svg width="16" height="16" viewBox="0 0 16 16"><rect x="2" y="2" width="12" height="12" fill="none" stroke="#0c2646" stroke-width="1.6"/><line x1="2" y1="5.5" x2="14" y2="5.5" stroke="#0c2646" stroke-width="1.6"/><line x1="5" y1="9" x2="11" y2="9" stroke="#0c2646" stroke-width="1.4"/><line x1="5" y1="11.5" x2="11" y2="11.5" stroke="#0c2646" stroke-width="1.4"/></svg></div>

  <div class="abs service" style="left:390px;top:63px">
    <h3>HOME SCHOOLSUPPORT</h3>
    <p>Vut sagittis a, magna ridiculus! Scelerisque parturient! Cum duis nunc in, dignissim, porta porta enim, proin turpis .</p>
  </div>
  <div class="abs service-icon" style="left:372px;top:72px"><svg width="16" height="16" viewBox="0 0 16 16"><path d="M2 6h3l7-4v12l-7-4H2z" fill="#0c2646"/><rect x="4" y="10" width="2.5" height="4" fill="#0c2646"/></svg></div>

  <div class="abs service" style="left:96px;top:144px">
    <h3>HOME SCHOOLSUPPORT</h3>
    <p>Vut sagittis a, magna ridiculus! Scelerisque parturient! Cum duis nunc in, dignissim, porta porta enim, proin turpis .</p>
  </div>
  <div class="abs service-icon" style="left:77px;top:152px"><svg width="16" height="16" viewBox="0 0 16 16"><rect x="1" y="3" width="10" height="8" fill="none" stroke="#0c2646" stroke-width="1.5"/><circle cx="13" cy="5" r="1.8" fill="#0c2646"/><rect x="11.5" y="7.5" width="3" height="6.5" fill="#0c2646"/><line x1="3" y1="9" x2="8" y2="5" stroke="#0c2646" stroke-width="1.3"/></svg></div>

  <div class="abs service" style="left:390px;top:145px">
    <h3>HOME SCHOOLSUPPORT</h3>
    <p>Vut sagittis a, magna ridiculus! Scelerisque parturient! Cum duis nunc in, dignissim, porta porta enim, proin turpis .</p>
  </div>
  <div class="abs service-icon" style="left:372px;top:154px"><svg width="16" height="16" viewBox="0 0 16 16"><rect x="2" y="7" width="3" height="7" fill="#0c2646"/><path d="M6 7l3-5c1.5 0 2 1 1.6 2.5L10 6.5h3.5c1 0 1.5.8 1.3 1.7l-1.2 4.8c-.2.7-.8 1-1.5 1H6z" fill="#0c2646"/></svg></div>
</section>

<section class="abs programs">
  <div class="abs program" style="left:74px;top:36px">
    <div class="abs program-photo" role="img" aria-label="Photo of a teacher helping children colour at a table" style="background:radial-gradient(ellipse 40% 50% at 45% 30%,#e8c2a8,rgba(232,194,168,0)),radial-gradient(ellipse 35% 45% at 85% 65%,#9b7ac4,rgba(155,122,196,0)),radial-gradient(ellipse 40% 40% at 15% 85%,#8fc24e,rgba(143,194,78,0)),linear-gradient(135deg,#d7cfc4,#b9a7b5 60%,#7a84b8)"></div>
    <p>Praesent arcu gravida vehicula est node maecenas loareet morbi a dosis luctus. Urna lacinia eleifend praesent .</p>
  </div>
  <div class="abs btn" style="left:105px;top:190px">Read More</div>

  <div class="abs program" style="left:220px;top:36px;height:163px">
    <div class="abs program-photo" role="img" aria-label="Photo of a toddler playing with shape blocks beside a teacher" style="background:radial-gradient(ellipse 35% 45% at 30% 45%,#c9e3b2,rgba(201,227,178,0)),radial-gradient(ellipse 40% 50% at 78% 40%,#c89a7c,rgba(200,154,124,0)),radial-gradient(ellipse 60% 30% at 50% 95%,#d97aa6,rgba(217,122,166,0)),linear-gradient(135deg,#a9c6de,#e3c9cf 55%,#c98aa4)"></div>
    <p style="top:88px">Praesent arcu gravida vehicula est node maecenas loareet morbi a dosis luctus. Urna lacinia eleifend praesent .</p>
  </div>
  <div class="abs btn" style="left:251px;top:190px">Read More</div>

  <div class="abs program" style="left:366px;top:36px;height:163px">
    <div class="abs program-photo" role="img" aria-label="Photo of children playing on a small indoor slide" style="background:radial-gradient(ellipse 30% 45% at 45% 70%,#e2463a,rgba(226,70,58,0)),radial-gradient(ellipse 25% 40% at 25% 60%,#5fae4c,rgba(95,174,76,0)),radial-gradient(ellipse 25% 30% at 55% 25%,#f0c838,rgba(240,200,56,0)),radial-gradient(ellipse 25% 40% at 80% 55%,#e6e2dc,rgba(230,226,220,0)),linear-gradient(135deg,#8c8a6a,#b89478 50%,#6f7f9a)"></div>
    <p style="top:87px">Praesent arcu gravida vehicula est node maecenas loareet morbi a dosis luctus. Urna lacinia eleifend praesent .</p>
  </div>
  <div class="abs btn" style="left:397px;top:190px">Read More</div>

  <div class="abs program" style="left:513px;top:35px;height:163px">
    <div class="abs program-photo" role="img" aria-label="Photo of a smiling boy playing in a classroom" style="background:radial-gradient(ellipse 30% 40% at 75% 80%,#4fae4a,rgba(79,174,74,0)),radial-gradient(ellipse 25% 35% at 72% 35%,#d9b08e,rgba(217,176,142,0)),radial-gradient(ellipse 35% 30% at 25% 85%,#c23a34,rgba(194,58,52,0)),linear-gradient(135deg,#e4dbd0,#c9b49c 50%,#a89a88)"></div>
    <p style="top:87px">Praesent arcu gravida vehicula est node maecenas loareet morbi a dosis luctus. Urna lacinia eleifend praesent .</p>
  </div>
  <div class="abs btn" style="left:545px;top:190px">Read More</div>
</section>

<section class="abs staff">
  <h2 class="abs section-title">Our Staff</h2>
  <p class="abs staff-intro">Praesent arcu gravida vehicula est node maecenas loareet morbi a dosis luctus. Urna eget lacinia eleifend praesent luctus a arcu quis facilisis venenatis aenean interdum.</p>

  <div class="abs member" style="left:115px;top:99px">
    <div class="avatar" role="img" aria-label="Portrait of staff member Dana Whitfield" style="background:radial-gradient(circle at 50% 55%,#f0d2bf 0 38%,#5a3a2a 70%,#f4f1ee 100%)"></div>
    <h4>Dana Whitfield</h4>
    <p>Sed diam nonummy nibh euismod</p>
  </div>
  <div class="abs member" style="left:276px;top:103px">
    <div class="avatar" role="img" aria-label="Portrait of staff member Laura Benning" style="background:radial-gradient(circle at 50% 58%,#eec6a8 0 36%,#a8744a 68%,#e9e2da 100%)"></div>
    <h4 style="margin-top:8px">Laura Benning</h4>
    <p>Diam nonummy nibh euismod tinc</p>
  </div>
  <div class="abs member" style="left:438px;top:105px">
    <div class="avatar" role="img" aria-label="Portrait of staff member Nadia Cole" style="background:radial-gradient(circle at 50% 58%,#a56c4c 0 36%,#2a1c16 70%,#eeeae6 100%)"></div>
    <h4 style="margin-top:6px">Nadia Cole</h4>
    <p>Nonummy nibh euismod tincidunt ut</p>
  </div>
</section>

<footer class="abs footer">Copyright © 2015 The Maplewood Learning House. Powered by SitePress and Brightloom</footer>

</body>
</html>
```